Marketing - Outdoor Vinyl banner, Outdoor Poster, Flyer modifications

Hi, I worked with you in the past and attached flyer designs. It just needs to be tweaked for various prints.
1)Outdoor vinyl banner (4 feet height and 8 feet width) print: Just grand opening pic, logo with name, tagline and call/text us portion.
2)Outdoor Poster (5 feet height and 3 feet width) print: same as above
3) Indoor poster for both horizontal & Vertical prints: Just logo w/ name, tagline, "We are MOVING Next door"
4)Flyer: will give minor modifications to attached flyer designs

```html
<!DOCTYPE html>
<html lang="en">
<head>
<meta charset="utf-8">
<title>Brightway Dental – We Are Moving Next Door</title>
<link href="https://fonts.googleapis.com/css2?family=Roboto+Slab:wght@700&display=swap" rel="stylesheet">
<style>
  :root {
    --canvas-bg: #e9ecef;
    --paper: #ffffff;
    --cyan: #0bb0d9;
    --slate: #5f7797;
    --navy: #2b405c;
    --ink-light: #ffffff;
  }
  html, body {
    margin: 0;
    padding: 0;
    width: 1096px;
    height: 1200px;
    overflow: hidden;
    background: var(--canvas-bg);
  }
  .poster {
    position: absolute;
    left: 184px;
    top: 40px;
    width: 928px;
    height: 1430px;
    transform: scale(0.7832);
    transform-origin: top left;
    background: var(--paper);
    overflow: hidden;
    font-family: "Roboto Slab", Georgia, serif;
    font-weight: 700;
  }
  .poster__waves {
    position: absolute;
    inset: 0;
    width: 928px;
    height: 1430px;
  }
  .brand {
    position: absolute;
    top: 118px;
    left: 0;
    width: 100%;
    display: flex;
    justify-content: center;
    align-items: center;
    gap: 22px;
  }
  .brand__dot {
    width: 64px;
    height: 64px;
    border-radius: 50%;
    background: var(--cyan);
  }
  .brand__name {
    color: var(--cyan);
    font-size: 64px;
    line-height: 1;
    letter-spacing: 1px;
  }
  .headline {
    position: absolute;
    top: 532px;
    left: 0;
    width: 100%;
    text-align: center;
    color: var(--ink-light);
    margin: 0;
  }
  .headline__lead {
    display: block;
    font-size: 70px;
    line-height: 1;
    letter-spacing: 0.5px;
  }
  .headline__main {
    display: block;
    font-size: 198px;
    line-height: 0.87;
    margin-top: 42px;
    letter-spacing: 1px;
  }
  .tagline {
    position: absolute;
    top: 1280px;
    left: 0;
    width: 100%;
    text-align: center;
    margin: 0;
    color: var(--cyan);
    font-size: 68px;
    line-height: 1;
  }
</style>
</head>
<body>
  <div class="poster">
    <svg class="poster__waves" viewBox="0 0 928 1430" aria-hidden="true">
      <path d="M0,184 C240,300 600,440 928,286 L928,1430 L0,1430 Z" fill="var(--cyan)"/>
      <path d="M0,194 C260,330 620,470 928,300 L928,1430 L0,1430 Z" fill="var(--paper)"/>
      <path d="M0,210 C270,360 640,490 928,318 L928,1430 L0,1430 Z" fill="var(--slate)"/>
      <path d="M0,226 C270,370 620,450 928,330 L928,1430 L0,1430 Z" fill="var(--cyan)"/>

      <path d="M0,962 C250,1140 620,1260 928,1070 L928,1430 L0,1430 Z" fill="var(--paper)"/>
      <path d="M0,978 C260,1160 620,1270 928,1084 L928,1430 L0,1430 Z" fill="var(--cyan)"/>
      <path d="M0,990 C260,1180 620,1290 928,1100 L928,1430 L0,1430 Z" fill="var(--navy)"/>
    </svg>

    <div class="brand">
      <span class="brand__dot"></span>
      <span class="brand__name">Brightway Dental</span>
    </div>

    <h1 class="headline">
      <span class="headline__lead">WE ARE MOVING</span>
      <span class="headline__main">NEXT<br>DOOR!</span>
    </h1>

    <p class="tagline">Excited to find home!</p>
  </div>
</body>
</html>
```